Graphical design for food product in 1 Liter carton

We need this design not for a real product but as a showcase for a new service.

This special situation makes it really simple for you to participate because you only have to care about how the visual impression of your design is.

Furthermore it gives you the opportunity to get an extra winning chance if you choose to also participate in the open competition at our website - where you can enter the same design as you enter here at ArtForge.

Here is the requirements:

1. You must apply your design to our attatched template

2. Make a design for a food product of your own choice, which is to be sold from retail stores in a rectangular 1 L carton – based on our template.

3. You are only allowed to use brand names and/or logos that you have the rights to use for this competition, so please make completely fictive brand names and logos.

4. Your design is evaluated on the visual impression only, which means that your text on the design can be in any language and doesn’t have to relate to the design.

5. The criteria for the evaluation of your design is your creativity, the graphical quality and how well the product will display it self in the stores.

If you also want to participate in the open competition on our website - where you can win an SlateTab Lite, and will get your design skills exposed to brand owners and packaging manufacturers all over the world, then please visit spinomodel.example/packaging-design-competition/

Attatched is:

A. Empty design template you must apply your design to. Remove the layer with our template when you return your send in your design.

B. Example of design applied to the template.

C. Example of the applied example design after it has been converted to 3D with our online 3D engine at SpinoModel.example.

The winning design will be converted to 3D and will be used as a showcase on our website - all designers can enter their design to our open competition at SpinoModel.example.

```html
<!DOCTYPE html>
<html lang="en">
<head>
<meta charset="utf-8">
<title>Orchard Leaf Pomegranate Ice Tea – Carton Panels</title>
<link rel="stylesheet" href="https://fonts.googleapis.com/css2?family=Cinzel:wght@700;900&family=Lilita+One&family=Arimo:wght@400;700&display=swap">
<style>
  :root {
    --bg: #8a8a8a;
    --paper: #fbfbf8;
    --band-red: #e04a4f;
    --band-pink: #f4a3a0;
    --splash-red: rgba(226, 64, 72, 0.85);
    --splash-pink: rgba(242, 120, 124, 0.75);
    --splash-orange: rgba(244, 150, 90, 0.55);
    --splash-lime: rgba(140, 198, 63, 0.7);
    --splash-green: rgba(92, 170, 48, 0.55);
    --leaf-green: #3f8f2a;
    --lime: #8cc63f;
    --text-dark: #4a2a1a;
    --text-red: #9c1c2a;
    --side-text: #333333;
    --fruit-deep: #9c1c2a;
    --fruit-bright: #d9364a;
  }
  * { margin: 0; padding: 0; box-sizing: border-box; }
  html, body { width: 1154px; height: 1200px; overflow: hidden; background: var(--bg); }
  .canvas { position: relative; width: 1154px; height: 1200px; }

  .panel { position: absolute; top: 60px; height: 1080px; background: var(--paper); overflow: hidden; }
  .panel-front { left: 57px; width: 620px; }
  .panel-side { left: 677px; width: 420px; border-left: 1px solid #e4e4e0; }

  .front-splash {
    position: absolute; inset: 0;
    background:
      radial-gradient(ellipse 260px 200px at 30% 14%, var(--splash-red), transparent 70%),
      radial-gradient(ellipse 300px 220px at 70% 10%, var(--splash-pink), transparent 72%),
      radial-gradient(ellipse 180px 160px at 92% 26%, var(--splash-lime), transparent 70%),
      radial-gradient(ellipse 160px 140px at 6% 30%, var(--splash-lime), transparent 70%),
      radial-gradient(ellipse 200px 120px at 85% 48%, var(--splash-orange), transparent 70%),
      radial-gradient(ellipse 150px 120px at 10% 52%, var(--splash-green), transparent 70%),
      radial-gradient(ellipse 240px 150px at 88% 80%, var(--splash-lime), transparent 70%),
      radial-gradient(ellipse 200px 140px at 12% 78%, var(--splash-orange), transparent 70%);
  }
  .band-bottom {
    position: absolute; left: 0; bottom: 0; width: 100%; height: 130px;
    background: linear-gradient(180deg, rgba(244,163,160,0) 0%, var(--band-pink) 30%, var(--band-red) 100%);
  }

  .claim {
    position: absolute; top: 140px; width: 100%; text-align: center;
    font-family: "Cinzel", serif; font-weight: 900; font-size: 32px; line-height: 1.3;
    color: var(--paper); letter-spacing: 1px;
  }

  .brand {
    position: absolute; top: 360px; width: 100%;
    display: flex; justify-content: center; align-items: center; gap: 14px;
  }
  .brand-dot { width: 44px; height: 44px; border-radius: 50%; background: var(--fruit-bright); }
  .brand-name {
    font-family: "Cinzel", serif; font-weight: 900; font-size: 58px; color: var(--leaf-green);
  }

  .flavour {
    position: absolute; top: 500px; left: 0; width: 100%; text-align: center;
    font-family: "Cinzel", serif; font-weight: 900; font-size: 32px; line-height: 1.35;
    color: var(--text-dark);
  }
  .product {
    position: absolute; top: 595px; left: 0; width: 100%; text-align: center;
    font-family: "Lilita One", sans-serif; font-size: 96px; line-height: 1; color: var(--leaf-green); letter-spacing: 2px;
  }
  .fruit-art {
    position: absolute; top: 730px; left: 150px; width: 400px; height: 200px; border-radius: 50%;
    background: radial-gradient(ellipse at 45% 40%, var(--fruit-bright), var(--fruit-deep) 65%, rgba(156,28,42,0) 100%);
  }
  .cert-badge {
    position: absolute; top: 870px; left: 40px; width: 72px; height: 72px; border-radius: 50%;
    background: #ffffff; border: 3px solid var(--leaf-green);
  }
  .benefits {
    position: absolute; bottom: 14px; width: 100%; text-align: center;
    font-family: "Cinzel", serif; font-weight: 700; font-size: 19px; line-height: 1.3; color: var(--text-red);
  }

  .side-splash {
    position: absolute; inset: 0;
    background:
      radial-gradient(ellipse 200px 220px at 85% 18%, var(--splash-pink), transparent 70%),
      radial-gradient(ellipse 140px 120px at 60% 8%, var(--splash-lime), transparent 70%),
      radial-gradient(ellipse 220px 200px at 25% 82%, var(--splash-lime), transparent 70%),
      radial-gradient(ellipse 180px 160px at 90% 70%, var(--splash-orange), transparent 70%);
  }
  .side-brand {
    position: absolute; top: 230px; width: 100%; text-align: center;
    font-family: "Cinzel", serif; font-weight: 900; font-size: 34px; color: var(--leaf-green);
  }
  .side-tagline {
    position: absolute; top: 360px; left: 40px; right: 40px;
    font-family: "Arimo", sans-serif; font-size: 22px; line-height: 1.3; color: var(--side-text);
  }
  .side-story {
    position: absolute; top: 460px; left: 40px; right: 40px;
    font-family: "Arimo", sans-serif; font-size: 20px; line-height: 1.45; color: var(--side-text);
  }
  .veg-badge {
    position: absolute; bottom: 150px; left: 60px; width: 48px; height: 48px; border-radius: 50%;
    background: var(--lime);
  }
</style>
</head>
<body>
<main class="canvas">
  <section class="panel panel-front">
    <div class="front-splash" role="img" aria-label="Vivid red, pink, orange and green watercolour paint splashes"></div>
    <div class="band-bottom"></div>
    <p class="claim">Sweetened with<br>Pure Agave</p>
    <div class="brand">
      <span class="brand-dot"></span>
      <span class="brand-name">Orchard Leaf</span>
    </div>
    <p class="flavour">Organic Amazon<br>Pomegranate</p>
    <p class="product">ICE TEA</p>
    <div class="fruit-art" role="img" aria-label="Illustration of a whole pomegranate with an opened half showing seeds"></div>
    <div class="cert-badge"></div>
    <p class="benefits">Low Glycemic<br>High in Antioxidants<br>Boosts Metabolism<br>Energizes &amp; Restores</p>
  </section>

  <section class="panel panel-side">
    <div class="side-splash" role="img" aria-label="Pink, orange and green watercolour paint splashes"></div>
    <p class="side-brand">Orchard Leaf</p>
    <p class="side-tagline">The World's Healthiest, Best Tasting Energy Tea</p>
    <p class="side-story">A simple brand story goes here. We will state our case for why Orchard Leaf Teas are superior. A simple brand story goes here. We will state our case for why Orchard Leaf Teas are superior. A simple brand story goes here. We will state why Orchard Leaf.</p>
    <div class="veg-badge"></div>
  </section>
</main>
</body>
</html>
```